Physician and Alternative Investments Investor needs a business card design.

I am making a career change from a plastic surgeon to a career as an investor. I am primarily involved with Angel Investing. I really want a fairly simple design overall and don't need to list angel investing unless it can be done very subtly, perhaps via an image rather than verbiage. A design without any mention of angel investing is completely acceptable. My credentials are "MD, MBA." I will also want to place my email address and mobile phone number and have provided below.

Target Market(s)

business contacts (physicians and non-physicians in the business world)

Industry/Entity Type

Business

Requirements
Must have
• Colin Pettigrew
• MD, MBA
• drcolinpettigrew@mailvane.net
• cell 770.548.2913
Should not have
• Clutter.

```html
<!DOCTYPE html>
<html lang="en">
<head>
<meta charset="utf-8">
<title>Colin Pettigrew – Business Card</title>
<link rel="stylesheet" href="https://fonts.googleapis.com/css2?family=Open+Sans:wght@400;600&family=Questrial&display=swap">
<style>
  :root {
    --backdrop-top: #2a2a2a;
    --backdrop-bottom: #050505;
    --card: #ffffff;
    --navy: #123d82;
    --ink: #1a1a1a;
    --muted: #555555;
    --rule: #a9a9a9;
  }
  * { margin: 0; padding: 0; box-sizing: border-box; }
  html, body { width: 1200px; height: 900px; overflow: hidden; }
  body {
    position: relative;
    background: linear-gradient(to bottom, var(--backdrop-top), var(--backdrop-bottom));
    font-family: "Open Sans", Arial, sans-serif;
  }
  .card {
    position: absolute;
    top: 306px;
    width: 439px;
    height: 271px;
    background: var(--card);
    border-radius: 10px;
  }
  .card--back { left: 149px; }
  .card--front { left: 609px; }

  .brand-mark {
    position: absolute;
    left: 0; right: 0;
    text-align: center;
    color: var(--navy);
    font-family: "Open Sans", Arial, sans-serif;
    font-weight: 600;
    letter-spacing: 0.04em;
  }
  .card--back .brand-mark { top: 84px; font-size: 24px; }
  .card--front .brand-mark { top: 76px; font-size: 20px; }

  .holder { position: absolute; left: 19px; top: 194px; }
  .holder__name { color: var(--navy); font-weight: 600; font-size: 15px; line-height: 20px; }
  .holder__credentials { color: var(--ink); font-size: 12px; line-height: 20px; }

  .contact { position: absolute; right: 30px; top: 197px; list-style: none; }
  .contact__item {
    display: flex; align-items: center; justify-content: flex-end; gap: 7px;
    color: var(--ink); font-size: 12px; line-height: 19px;
  }
  .contact__icon { width: 13px; height: 13px; display: block; }

  .front-name {
    position: absolute; left: 0; right: 0; top: 160px;
    text-align: center; color: var(--navy);
    font-family: "Questrial", "Century Gothic", sans-serif;
    font-size: 32px; line-height: 38px; letter-spacing: 0.01em;
  }
  .front-credentials {
    position: absolute; left: 109px; width: 222px; top: 198px;
    display: flex; align-items: center; gap: 6px;
    color: var(--muted);
    font-family: "Questrial", "Century Gothic", sans-serif;
    font-size: 14px; letter-spacing: 0.06em;
  }
  .front-credentials::before, .front-credentials::after {
    content: ""; flex: 1; height: 1px; background: var(--rule);
  }
</style>
</head>
<body>
  <section class="card card--back" aria-label="Card back with contact details">
    <p class="brand-mark">Pettigrew Ventures</p>
    <div class="holder">
      <p class="holder__name">Colin Pettigrew</p>
      <p class="holder__credentials">MD, MBA</p>
    </div>
    <ul class="contact">
      <li class="contact__item">770.548.2913
        <svg class="contact__icon" viewBox="0 0 13 13" aria-hidden="true">
          <rect width="13" height="13" rx="1.5" fill="#123d82"/>
          <path d="M3 5.2c0-1.2 1.6-1.8 3.5-1.8S10 4 10 5.2v.6H8.4v-.8H4.6v.8H3z M4 6.6h5l.8 3H3.2z" fill="#fff"/>
        </svg>
      </li>
      <li class="contact__item">drcolinpettigrew@mailvane.net
        <svg class="contact__icon" viewBox="0 0 13 13" aria-hidden="true">
          <rect width="13" height="13" rx="1.5" fill="#123d82"/>
          <rect x="3" y="4" width="7" height="5" fill="#fff"/>
          <path d="M3 4l3.5 2.8L10 4" fill="none" stroke="#123d82" stroke-width="0.8"/>
        </svg>
      </li>
    </ul>
  </section>

  <section class="card card--front" aria-label="Card front">
    <p class="brand-mark">Pettigrew Ventures</p>
    <h1 class="front-name">Colin Pettigrew</h1>
    <p class="front-credentials">MD, MBA</p>
  </section>
</body>
</html>
```